Psychotherapist need a business card with logo

I am a psychotherapist in need of a business card. The card must have:

Marisol Trevuneda
Psicoterapeuta
937 281 706

Psychologists use the greek letter psy, which is the psychologist symbol, but I would prefer something like a mandala, a graphic symbol, an iconic tree, nothing very usual, but something that shows confidence and trust.

Industry/Entity Type

Business

```html
<!DOCTYPE html>
<html lang="es">
<head>
<meta charset="utf-8">
<title>Marisol Trevuneda – Psicoterapeuta</title>
<link href="https://fonts.googleapis.com/css2?family=Montserrat:wght@300;700&display=swap" rel="stylesheet">
<style>
  :root {
    --page-bg: #e9e4de;
    --dark-card: #121212;
    --dark-card-edge: #232323;
    --olive: #5b5a26;
    --olive-soft: #45441f;
    --lime: #c6d22c;
    --blue-top: #22b3ea;
    --blue-bottom: #1a7fcf;
    --blue-deco: #7cc6ee;
    --blue-deco-soft: #4aa8e2;
    --white: #ffffff;
    --ink: #1b1b1b;
  }
  * { box-sizing: border-box; margin: 0; padding: 0; }
  html, body { width: 1200px; height: 1000px; overflow: hidden; }
  body {
    background: var(--page-bg);
    font-family: "Montserrat", Arial, sans-serif;
    position: relative;
  }
  .card {
    position: absolute;
    width: 540px;
    height: 310px;
    border-radius: 22px;
    overflow: hidden;
    box-shadow: 0 10px 28px rgba(0,0,0,.22);
  }
  .card--dark { left: 45px; top: 110px; background: linear-gradient(135deg, var(--dark-card-edge), var(--dark-card) 60%); }
  .card--blue { left: 615px; top: 110px; background: linear-gradient(160deg, var(--blue-top), var(--blue-bottom)); }

  .card__ornament {
    position: absolute;
    width: 380px; height: 380px;
    left: -120px; top: 20px;
    border-radius: 50%;
  }
  .card--dark .card__ornament { background: radial-gradient(circle, var(--olive-soft) 0 55%, var(--olive) 56% 100%); }
  .card--blue .card__ornament { background: radial-gradient(circle, var(--blue-deco-soft) 0 55%, var(--blue-deco) 56% 100%); opacity: .75; }

  .identity {
    position: absolute;
    right: 40px; top: 34px;
    width: 250px;
    text-align: center;
    color: var(--white);
  }
  .identity__mark {
    width: 40px; height: 40px;
    border-radius: 50%;
    margin: 0 auto 8px;
  }
  .card--dark .identity__mark { background: var(--lime); }
  .card--blue .identity__mark { background: var(--white); }
  .identity__name { font-weight: 700; font-size: 21px; letter-spacing: -.2px; }
  .identity__rule { height: 1px; margin: 8px 0 8px; }
  .card--dark .identity__rule { background: var(--lime); }
  .card--blue .identity__rule { background: var(--white); opacity: .8; }
  .identity__role { font-weight: 300; font-size: 12px; letter-spacing: 6px; }

  .contact {
    position: absolute;
    right: 48px; top: 190px;
    display: flex; align-items: center; gap: 12px;
    color: var(--white);
    font-size: 22px; font-weight: 300;
  }
  .contact__icon { width: 22px; height: 22px; }

  .lockup {
    position: absolute;
    left: 0; right: 0; top: 560px;
    text-align: center;
    color: var(--ink);
  }
  .lockup__mark {
    width: 90px; height: 90px; border-radius: 50%;
    background: var(--lime);
    margin: 0 auto 22px;
  }
  .lockup__name { font-weight: 700; font-size: 38px; }
  .lockup__rule { width: 340px; height: 1px; background: var(--lime); margin: 14px auto; }
  .lockup__role { font-weight: 300; font-size: 20px; letter-spacing: 9px; }
</style>
</head>
<body>

<section class="card card--dark">
  <div class="card__ornament" role="img" aria-label="Large faint mandala ornament in olive tones"></div>
  <div class="identity">
    <div class="identity__mark"></div>
    <div class="identity__name">Marisol Trevuneda</div>
    <div class="identity__rule"></div>
    <div class="identity__role">Psicoterapeuta</div>
  </div>
  <div class="contact">
    <svg class="contact__icon" viewBox="0 0 24 24" aria-hidden="true"><circle cx="12" cy="12" r="11" fill="#c6d22c"/><rect x="8.5" y="5.5" width="7" height="13" rx="1.5" fill="none" stroke="#121212" stroke-width="1.6"/><line x1="11" y1="16" x2="13" y2="16" stroke="#121212" stroke-width="1.4"/></svg>
    <span>937 281 706</span>
  </div>
</section>

<section class="card card--blue">
  <div class="card__ornament" role="img" aria-label="Large faint mandala ornament in light blue tones"></div>
  <div class="identity">
    <div class="identity__mark"></div>
    <div class="identity__name">Marisol Trevuneda</div>
    <div class="identity__rule"></div>
    <div class="identity__role">Psicoterapeuta</div>
  </div>
  <div class="contact">
    <svg class="contact__icon" viewBox="0 0 24 24" aria-hidden="true"><circle cx="12" cy="12" r="11" fill="#ffffff"/><rect x="8.5" y="5.5" width="7" height="13" rx="1.5" fill="none" stroke="#1a7fcf" stroke-width="1.6"/><line x1="11" y1="16" x2="13" y2="16" stroke="#1a7fcf" stroke-width="1.4"/></svg>
    <span>937 281 706</span>
  </div>
</section>

<section class="lockup">
  <div class="lockup__mark"></div>
  <div class="lockup__name">Marisol Trevuneda</div>
  <div class="lockup__rule"></div>
  <div class="lockup__role">Psicoterapeuta</div>
</section>

</body>
</html>
```